Design for a creative video production company !!

Looking for a 3-4 page layout for my project proposals. Should include :
Cover page
Page 1: is the general overview (see attached)
Page 2: Project Outline ( a blank area to add project specifics)
Page 3: budget (a blank table here I can add in the numbers)

final version a pdf I can edit. even just a page design I can add as my background. More info on company please go to www.brightharbourfilms.example

Target Market(s)

Marketing managers, communications people, people who want to use video ... professional video to tell their story or educate.

Industry/Entity Type

It Company

Font styles to use
Serif
Sans Serif

Colors

Designer to choose colors to be used in the design.

Requirements
Must have
• Must have a way I can fill in the information later, I'm happy to use a background and leave an area black I can add a table for budgets. Would like to see a pie chart or graph used to show the time of each stage of the project. See general overview doc attached.
Nice to have
• A variation of the proposal I attached is just a start, Please look at website, (brightharbourfilms.example) business cards, and proposal as an idea of the branding.
Should not have
• sad clowns

```html
<!DOCTYPE html>
<html lang="en">
<head>
<meta charset="utf-8">
<title>Bright Harbour Films – General Overview</title>
<link href="https://fonts.googleapis.com/css2?family=Open+Sans:ital,wght@0,600;0,700;1,600&family=Ubuntu:ital,wght@0,500;0,700;1,700&display=swap" rel="stylesheet">
<style>
  :root{
    --red:#e3141b;
    --ink:#2b2b2b;
    --page:#e8e8ea;
    --band-top:#9a9a9c;
    --band-bottom:#68686a;
    --footer:#38393b;
    --footer-left:#565759;
    --green:#5cbb47;
    --orange:#f7992a;
    --blue:#28b2e6;
    --crimson:#e4294b;
    --legend:#555;
  }
  *{margin:0;padding:0;box-sizing:border-box}
  html,body{width:927px;height:1200px;overflow:hidden;background:var(--page)}
  .page{position:relative;width:927px;height:1200px;background:var(--page);font-family:"Open Sans",Arial,sans-serif;color:var(--ink)}
  .intro{position:absolute;left:0;top:0;width:927px;height:191px;
    background:linear-gradient(to bottom,var(--band-top),var(--band-bottom));
    color:#fff;font-weight:700;font-size:16px;line-height:21.5px;text-align:center;padding:34px 60px 0}
  .intro p+p{margin-top:12px}
  .stage{position:absolute;width:400px}
  .stage-title{position:absolute;left:0;top:0;font-family:"Ubuntu",sans-serif;font-weight:700;color:var(--red);font-size:19.5px;line-height:22.5px;padding-left:28px}
  .stage-title em{font-style:italic}
  .chevron{position:absolute;left:0;top:10px;width:22px;height:22px}
  .stage-body{position:absolute;left:0;border-left:2px solid var(--red);padding-left:13px;width:400px}
  .role-head{font-family:"Ubuntu",sans-serif;font-weight:500;font-size:20.5px;line-height:24px;color:var(--ink);margin-bottom:4px}
  .role-text{font-size:13.6px;line-height:18.2px;font-weight:600}
  .note{position:absolute;left:13px;font-size:10px;font-style:italic;font-weight:600}
  .payment-title{position:absolute;left:56px;top:846px;font-family:"Ubuntu",sans-serif;font-weight:700;font-size:28px;color:var(--red);padding-left:28px}
  .payment-title .chevron{top:9px}
  .payment-body{position:absolute;left:56px;top:895px;border-left:2px solid var(--red);padding-left:10px;width:540px;height:153px;font-weight:600}
  .payment-lead{font-size:15.2px;line-height:21px}
  .milestones{display:grid;grid-template-columns:190px 200px;font-size:15px;line-height:20.5px;margin-top:6px;list-style:none}
  .milestones li::before{content:"•";margin-right:7px}
  .payment-note{font-size:13.6px;line-height:18.5px;margin-top:12px}
  .pie{position:absolute;left:587px;top:889px;width:160px;height:160px}
  .legend{position:absolute;left:758px;top:918px;list-style:none;font-family:"Open Sans",sans-serif;font-size:14px;line-height:18.5px;color:var(--legend)}
  .legend li{position:relative;padding-left:17px}
  .legend .swatch{position:absolute;left:0;top:4px;width:11px;height:11px}
  .footer{position:absolute;left:0;top:1115px;width:927px;height:39px;background:var(--footer)}
  .footer svg{position:absolute;left:0;top:0}
  .contact{position:absolute;right:45px;top:9px;color:#fff;font-weight:700;font-size:16px}
</style>
</head>
<body>
<div class="page">
  <header class="intro">
    <p>At Bright Harbour Films, we take a creative, collaborative, planned approach to creating exceptional videos. We take you on a journey from start to finish, guiding you through the stages, and eliminating the element of surprise (other than the final reveal!).</p>
    <p>Our goal is to give you the peace of mind that we will tell your vision and message.Here are the 4 stages that you can expect with a breakdown of the time usually required at each stage</p>
  </header>

  <!-- Stage 1 -->
  <section class="stage" style="left:56px;top:220px">
    <svg class="chevron" viewBox="0 0 22 22"><path d="M1 2h6l8 9-8 9H1l8-9z M8 2h5l8 9-8 9H8" fill="var(--red)"/></svg>
    <h2 class="stage-title">Stage 1:<br><em>Collaboration + Script development</em></h2>
    <div class="stage-body" style="top:65px;height:229px">
      <h3 class="role-head">Bright Harbour Films’ role:</h3>
      <p class="role-text">We seek to understand the CTA, the audience, your product/service and your brand. Armed with this understanding, we then work backwards, to develop and bring the script to life.</p>
      <h3 class="role-head" style="margin-top:19px">Your role:</h3>
      <p class="role-text">Act as a collaborator to help us capture your idea, provide context, information and research to help us understand your story.</p>
      <p class="note" style="top:216px">(This stage accounts for approx. 40 % of the overall project time).</p>
    </div>
  </section>

  <!-- Stage 2 -->
  <section class="stage" style="left:496px;top:220px">
    <svg class="chevron" viewBox="0 0 22 22"><path d="M1 2h6l8 9-8 9H1l8-9z M8 2h5l8 9-8 9H8" fill="var(--red)"/></svg>
    <h2 class="stage-title">Stage 2:<br><em>Pre-production</em></h2>
    <div class="stage-body" style="top:65px;height:229px">
      <h3 class="role-head">Bright Harbour Films’ role:</h3>
      <p class="role-text">in preparation for the shoot, handle logistics (location, equipment rentals, crew, talent, other).</p>
      <h3 class="role-head" style="margin-top:19px">Your role:</h3>
      <p class="role-text">As applicable, liaising with talent, organizing locations in conjunction with Bright Harbour Films, other.</p>
      <p class="note" style="top:216px">(This stage accounts for approx. 15 % of the overall project time).</p>
    </div>
  </section>

  <!-- Stage 3 -->
  <section class="stage" style="left:56px;top:547px">
    <svg class="chevron" viewBox="0 0 22 22"><path d="M1 2h6l8 9-8 9H1l8-9z M8 2h5l8 9-8 9H8" fill="var(--red)"/></svg>
    <h2 class="stage-title">Stage 3:<br><em>Filming</em></h2>
    <div class="stage-body" style="top:65px;height:208px">
      <h3 class="role-head">Bright Harbour Films’ role:</h3>
      <p class="role-text">directing and filming, managing all on-site parties, coaching talent, other.</p>
      <h3 class="role-head" style="margin-top:28px">Your role:</h3>
      <p class="role-text">attend as needed to ensure messaging is on point. Also, a chance to be part of the action!<br>Capture “behind the scenes” as needed.</p>
      <p class="note" style="top:195px">(This stage accounts for approx.15 % of the overall project t time).</p>
    </div>
  </section>

  <!-- Stage 4 -->
  <section class="stage" style="left:496px;top:547px">
    <svg class="chevron" viewBox="0 0 22 22"><path d="M1 2h6l8 9-8 9H1l8-9z M8 2h5l8 9-8 9H8" fill="var(--red)"/></svg>
    <h2 class="stage-title">Stage 4:<br><em>Pre-production</em></h2>
    <div class="stage-body" style="top:65px;height:208px">
      <h3 class="role-head">Bright Harbour Films’ role:</h3>
      <p class="role-text">Culling the raw footage into a compelling, concise finished product, in alignment with the final script. This is also when animation occurs (if applicable).</p>
      <h3 class="role-head" style="margin-top:10px">Your role:</h3>
      <p class="role-text">There are 2 screenings included in the quote. All feedback is captured and addressed online.</p>
      <p class="note" style="top:195px">(This stage accounts for approx.40% of the overall project time).</p>
    </div>
  </section>

  <!-- Payment -->
  <h2 class="payment-title">
    <svg class="chevron" viewBox="0 0 22 22"><path d="M1 2h6l8 9-8 9H1l8-9z M8 2h5l8 9-8 9H8" fill="var(--red)"/></svg>
    Payment process:
  </h2>
  <div class="payment-body">
    <p class="payment-lead">For projects under 30 days, payment is due upon project completion.<br>&nbsp;For projects over 30 days, we invoice at the following milestones:</p>
    <ul class="milestones">
      <li>upon script approval</li>
      <li>prior to pre-production</li>
      <li>upon shootcompletion</li>
      <li>after 2 screenings</li>
    </ul>
    <p class="payment-note">If additional screenings are required, additional hours are $x. Upon receiving final payment, the watermark is removed from the final version.</p>
  </div>

  <svg class="pie" viewBox="0 0 160 160" role="img" aria-label="Pie chart of project time by stage">
    <g stroke="var(--page)" stroke-width="6" stroke-linejoin="round">
      <path d="M80 80 L80 0 A80 80 0 0 1 145.5 125.9 Z" fill="var(--green)"/>
      <path d="M80 80 L145.5 125.9 A80 80 0 0 1 28.6 141.3 Z" fill="var(--orange)"/>
      <path d="M80 80 L28.6 141.3 A80 80 0 0 1 4.8 52.6 Z" fill="var(--blue)"/>
      <path d="M80 80 L4.8 52.6 A80 80 0 0 1 80 0 Z" fill="var(--crimson)"/>
    </g>
  </svg>
  <ul class="legend">
    <li><span class="swatch" style="background:var(--green)"></span>Collaboration +<br>Script development</li>
    <li><span class="swatch" style="background:var(--orange)"></span>Pre-production</li>
    <li><span class="swatch" style="background:var(--blue)"></span>Filming</li>
    <li><span class="swatch" style="background:var(--crimson)"></span>Editing</li>
  </ul>

  <footer class="footer">
    <svg width="260" height="39" viewBox="0 0 260 39">
      <polygon points="0,0 240,0 212,39 0,39" fill="var(--footer-left)"/>
      <polygon points="240,0 248,0 220,39 212,39" fill="#fff"/>
    </svg>
    <p class="contact">Ph: 555 014 2290 | www.brightharbourfilms.example</p>
  </footer>
</div>
</body>
</html>
```